City department needs a bold and eye-catching poster design.

We need a poster to promote a survey targeting youth and young adults from 14-29 yr olds in the city of Strathcona County. We want poster designs that are bold, provocative and colourful. We want to poster to be a bright piece of art on the wall. See images attached. REQUIRED COPY: "Need something? We're listening" OR "Have Ideas? We're listening" OR "Your Wish? We're listening"

Target Market(s)

Youth, 14-29 yr olds

Industry/Entity Type

Government

Font styles to use
Sans Serif

Requirements
Must have
• REQUIRED COPY: Need something? We're listening"

```html
<!DOCTYPE html>
<html lang="en">
<head>
<meta charset="utf-8">
<title>Need Something? We're Listening</title>
<link rel="stylesheet" href="https://fonts.googleapis.com/css2?family=Open+Sans:wght@700;800&display=swap">
<style>
  :root {
    --paper: #ffffff;
    --ink: #000000;
    --red: #e81c0a;
    --magenta: #b5146b;
    --orange: #ffa000;
    --yellow: #ffd200;
    --green: #7fdc0a;
    --sky: #00c8ff;
    --blue: #0055b0;
  }
  * { margin: 0; padding: 0; box-sizing: border-box; }
  html, body { width: 890px; height: 1200px; overflow: hidden; background: var(--paper); }
  .poster {
    position: relative;
    width: 890px;
    height: 1200px;
    background: var(--paper);
    font-family: "Open Sans", Arial, sans-serif;
    color: var(--ink);
  }
  .poster__art {
    position: absolute;
    inset: 0;
    width: 890px;
    height: 1200px;
  }
  .headline {
    font-family: "Open Sans", Arial, sans-serif;
    font-weight: 700;
    font-size: 124px;
    fill: var(--ink);
  }
  .sponsor {
    position: absolute;
    left: 0;
    right: 0;
    top: 960px;
    display: flex;
    align-items: center;
    justify-content: center;
    gap: 10px;
    font-weight: 700;
    font-size: 20px;
    color: var(--ink);
  }
  .sponsor__dot {
    width: 22px;
    height: 22px;
    border-radius: 50%;
    background: var(--orange);
  }
  .tagline {
    position: absolute;
    left: 0;
    right: 0;
    top: 1062px;
    text-align: center;
    font-weight: 700;
    font-size: 66px;
    line-height: 1;
    letter-spacing: 0.5px;
    color: var(--ink);
  }
</style>
</head>
<body>
<main class="poster">
  <svg class="poster__art" viewBox="0 0 1092 1472" xmlns="http://www.w3.org/2000/svg">
    <defs>
      <linearGradient id="mind-gradient" x1="0" y1="0" x2="1" y2="1">
        <stop offset="0" stop-color="var(--magenta)"/>
        <stop offset="0.3" stop-color="var(--red)"/>
        <stop offset="0.55" stop-color="var(--orange)"/>
        <stop offset="0.75" stop-color="var(--green)"/>
        <stop offset="1" stop-color="var(--blue)"/>
      </linearGradient>
      <path id="headline-path" d="M 225,290 Q 390,150 560,170 C 700,180 790,260 795,420 C 800,560 720,660 600,730 C 520,790 490,850 490,960 L 490,1090"/>
    </defs>
    <circle class="mind-illustration" role="img" aria-label="Illustration of a head in profile filled with colourful swirling shapes" cx="500" cy="540" r="320" fill="url(#mind-gradient)"/>
    <text class="headline">
      <textPath href="#headline-path" textLength="1440" lengthAdjust="spacing">NEED SOMETHING?</textPath>
    </text>
  </svg>

  <div class="sponsor">
    <span class="sponsor__dot"></span>
    <span class="sponsor__name">Riverbend County</span>
  </div>

  <h1 class="tagline">WE'RE LISTENING</h1>
</main>
</body>
</html>
```